Wedding Day Custom Wine Label - Tasmanian (Tamar Valley) wine

I am looking for a custom design that will be put on a wine label to commemorate a very good friend's wedding day.

We will need to be able to take the design and print it on to sticker labels that we can put on to wine bottles.

The bride and groom have asked for a simplistic label design (see example image attached). We need two labels. One for "Pinot Noir" wine and the other for "Chardonnay" wine. We would like the label to say:

The Hartwell's
Pinot Noir
2023
Tamar Valley

and for for the other wine variety:

The Hartwell's
Chardonnay
2023
Tamar Valley

smaller text below to say:

13.5% ALC/VOL 750ML
MEGAN & LIAM - 31.10.2024

I am happy to consider other variations - the bride & groom would prefer something minimalistic. Elegant and classy.

Target Market(s)

the bride & groom

Requirements
Must have
• Wedding date (31.10.2024). Wine type (Pinot Noir or Chardonnay).
Should not have
• images not essential

```html
<!DOCTYPE html>
<html lang="en">
<head>
<meta charset="utf-8">
<title>The Hartwell's – Wedding Wine Labels</title>
<link rel="stylesheet" href="https://fonts.googleapis.com/css2?family=Abril+Fatface&family=Allura&family=Cormorant+Garamond:wght@500;600&display=swap">
<style>
  :root {
    --backdrop: #a9a9a9;
    --paper: #fbfaf8;
    --blush: #f6dede;
    --gold: #d2a23c;
    --ink: #161414;
    --rose: #e0a793;
    --leaf: #5f9c8a;
    --sage: #b8c7a6;
  }
  * { margin: 0; padding: 0; box-sizing: border-box; }
  html, body { width: 1105px; height: 1200px; overflow: hidden; }
  body {
    background: var(--backdrop);
    display: flex;
    align-items: center;
    justify-content: center;
    gap: 45px;
  }
  .label {
    position: relative;
    width: 480px;
    height: 585px;
    background:
      radial-gradient(ellipse 55% 40% at 85% 85%, rgba(246, 222, 222, .7), transparent 70%),
      radial-gradient(ellipse 45% 35% at 20% 35%, rgba(246, 222, 222, .6), transparent 70%),
      var(--paper);
    box-shadow: 10px 8px 14px rgba(0, 0, 0, .35);
    overflow: hidden;
  }
  .label__frame { position: absolute; inset: 0; }
  .label__floral-top {
    position: absolute; left: 0; top: 0; width: 250px; height: 270px;
    background:
      radial-gradient(circle at 28% 28%, var(--rose) 0 16%, transparent 30%),
      radial-gradient(circle at 55% 13%, var(--rose) 0 8%, transparent 18%),
      radial-gradient(ellipse at 35% 40%, rgba(95, 156, 138, .55), transparent 62%);
    border-bottom-right-radius: 100% 100%;
  }
  .label__floral-bottom {
    position: absolute; right: 0; bottom: 0; width: 170px; height: 300px;
    background:
      radial-gradient(ellipse at 80% 80%, rgba(95, 156, 138, .7), transparent 58%),
      radial-gradient(ellipse at 75% 30%, rgba(184, 199, 166, .6), transparent 60%);
    border-top-left-radius: 100% 100%;
  }
  .label__text {
    position: absolute; left: 0; right: 0; top: 200px;
    text-align: center; color: var(--ink);
  }
  .label__house {
    font-family: "Abril Fatface", serif;
    font-size: 40px; letter-spacing: .5px; line-height: 1;
  }
  .label__details {
    margin-top: 10px;
    font-family: "Abril Fatface", serif;
    font-size: 22px; line-height: 26px;
  }
  .label__divider {
    display: block; margin: 36px auto 0;
  }
  .label__couple {
    margin-top: 18px;
    font-family: "Allura", cursive;
    font-size: 52px; line-height: 1;
  }
  .label__date {
    display: inline-block;
    margin-top: 0;
    padding: 0 22px 1px;
    border-bottom: 1px solid var(--ink);
    font-family: "Cormorant Garamond", serif;
    font-weight: 600; font-size: 12.5px; letter-spacing: .5px;
  }
  .label__spec {
    margin-top: 12px;
    font-family: "Cormorant Garamond", serif;
    font-weight: 600; font-size: 12.5px; line-height: 14px; letter-spacing: .6px;
  }
</style>
</head>
<body>

  <section class="label label--chardonnay">
    <div class="label__floral-top" role="img" aria-label="Watercolour roses and eucalyptus leaves"></div>
    <div class="label__floral-bottom" role="img" aria-label="Watercolour eucalyptus and fern foliage"></div>
    <svg class="label__frame" viewBox="0 0 480 585" aria-hidden="true">
      <polygon points="44,22 418,22 456,60 456,556 100,556 44,500" fill="none" stroke="var(--gold)" stroke-width="1.6"/>
      <polygon points="34,36 404,36 444,76 444,568 114,568 58,512 58,36" fill="none" stroke="var(--gold)" stroke-width="1.6"/>
    </svg>
    <div class="label__text">
      <h1 class="label__house">THE HARTWELL'S</h1>
      <p class="label__details">CHARDONNAY<br>TAMAR VALLEY<br>2023</p>
      <svg class="label__divider" width="96" height="6" viewBox="0 0 96 6" aria-hidden="true">
        <line x1="0" y1="3" x2="42" y2="3" stroke="var(--ink)" stroke-width="1.2"/>
        <circle cx="48" cy="3" r="2" fill="var(--ink)"/>
        <line x1="54" y1="3" x2="96" y2="3" stroke="var(--ink)" stroke-width="1.2"/>
      </svg>
      <p class="label__couple">Megan &amp; Liam</p>
      <p class="label__date">31.10.2024</p>
      <p class="label__spec">13.5% ALC/VOL<br>750ML</p>
    </div>
  </section>

  <section class="label label--pinot-noir">
    <div class="label__floral-top" role="img" aria-label="Watercolour roses and eucalyptus leaves"></div>
    <div class="label__floral-bottom" role="img" aria-label="Watercolour eucalyptus and fern foliage"></div>
    <svg class="label__frame" viewBox="0 0 480 585" aria-hidden="true">
      <polygon points="44,22 418,22 456,60 456,556 100,556 44,500" fill="none" stroke="var(--gold)" stroke-width="1.6"/>
      <polygon points="34,36 404,36 444,76 444,568 114,568 58,512 58,36" fill="none" stroke="var(--gold)" stroke-width="1.6"/>
    </svg>
    <div class="label__text">
      <h1 class="label__house">THE HARTWELL'S</h1>
      <p class="label__details">PINOT NOIR<br>TAMAR VALLEY<br>2023</p>
      <svg class="label__divider" width="96" height="6" viewBox="0 0 96 6" aria-hidden="true">
        <line x1="0" y1="3" x2="42" y2="3" stroke="var(--ink)" stroke-width="1.2"/>
        <circle cx="48" cy="3" r="2" fill="var(--ink)"/>
        <line x1="54" y1="3" x2="96" y2="3" stroke="var(--ink)" stroke-width="1.2"/>
      </svg>
      <p class="label__couple">Megan &amp; Liam</p>
      <p class="label__date">31.10.2024</p>
      <p class="label__spec">13.5% ALC/VOL<br>750ML</p>
    </div>
  </section>

</body>
</html>
```